A3 Event Poster for School Fundraiser

We are looking for a bold, engaging, and professional A3 poster design to promote a special school fundraising event. A top athlete will be visiting a primary school to inspire children, encourage participation in sport, and help launch a fundraising initiative to raise money for new PE/sports equipment for the school.

The poster will be displayed prominently outside the school and shared with parents and families. Its purpose is to generate excitement, explain the event quickly, and encourage parents/families to sponsor and get involved.

We work with about 50 different athletes so will need the design to be easy to alter the picture of the athlete/name etc so it can be replicated across the different athletes.

Target Market(s)

Priamary School Parents/Communities

Industry/Entity Type

Education

Font styles to use
Other font styles liked:
• The logo font is Rajdhani. ‘Corvel’ is bold, ‘Pennix’ is semibold and the strapline is regular.

Requirements
Must have
• Space for the Event Date (that school can write in themselves), A picture of the visiting athlete and their bio (with ability to easily change)
Nice to have
• Bold, eye-catching

```html
<!DOCTYPE html>
<html lang="en">
<head>
<meta charset="UTF-8">
<title>Inspirational athlete visiting our school</title>
<link rel="stylesheet" href="https://fonts.googleapis.com/css2?family=Inter:wght@400;500;600;700;800&display=swap">
<style>
  :root {
    --purple: #4a2096;
    --paper: #f4f4f3;
    --red: #d5190f;
    --pink: #ec7fa4;
    --blue: #0a70c2;
    --navy: #1c3f86;
    --ink: #111111;
    --muted: #3a3a3a;
    --white: #ffffff;
  }
  * { margin: 0; padding: 0; box-sizing: border-box; }
  html, body { width: 1200px; height: 754px; overflow: hidden; background: var(--paper); }
  .poster {
    position: relative;
    width: 1200px;
    height: 754px;
    overflow: hidden;
    background: var(--paper);
    font-family: "Inter", Arial, sans-serif;
  }
  .poster__backdrop { position: absolute; inset: 0; }
  .athlete-photo {
    position: absolute;
    left: 10px;
    top: 95px;
    width: 440px;
    height: 659px;
    border-radius: 200px 200px 0 0;
    background: linear-gradient(160deg, #6b4a3a 0%, #3b2a26 28%, var(--navy) 45%, #233f8a 70%, #c7362a 100%);
  }
  .impact-stat {
    position: absolute;
    left: 30px;
    top: 26px;
    display: flex;
    align-items: center;
    color: var(--white);
  }
  .impact-stat__number {
    font-size: 92px;
    font-weight: 800;
    line-height: 1;
    letter-spacing: -2px;
  }
  .impact-stat__label {
    margin-left: 8px;
    font-size: 23px;
    font-weight: 700;
    line-height: 24px;
    letter-spacing: -0.3px;
  }
  .athlete-bio {
    position: absolute;
    left: 700px;
    top: 56px;
    width: 456px;
    color: var(--muted);
  }
  .athlete-bio__name {
    color: var(--purple);
    font-size: 22px;
    font-weight: 800;
    line-height: 28px;
  }
  .athlete-bio__text {
    margin-top: 6px;
    font-size: 15px;
    font-weight: 500;
    line-height: 21px;
  }
  .headline {
    position: absolute;
    left: 590px;
    top: 222px;
    color: var(--red);
    font-size: 86px;
    font-weight: 700;
    line-height: 82px;
    letter-spacing: -1.2px;
  }
  .fundraiser {
    position: absolute;
    left: 594px;
    top: 488px;
    width: 560px;
    color: var(--ink);
    font-size: 18px;
    font-weight: 600;
    line-height: 24px;
  }
  .fundraiser strong { color: var(--blue); font-weight: 800; }
  .pillars {
    position: absolute;
    top: 550px;
    left: 592px;
    display: flex;
    gap: 20px;
  }
  .pillar {
    height: 92px;
    border-radius: 8px;
    display: flex;
    align-items: center;
    justify-content: center;
    text-align: center;
    color: var(--white);
    font-size: 27px;
    font-weight: 700;
    line-height: 32px;
  }
  .pillar--inspired { width: 173px; background: var(--pink); }
  .pillar--difference { width: 185px; background: var(--blue); }
  .pillar--active { width: 166px; background: linear-gradient(90deg, #e6508f 0%, #8a6cc0 55%, var(--blue) 100%); }
  .event-date {
    position: absolute;
    left: 592px;
    top: 678px;
    width: 565px;
    height: 59px;
    display: flex;
    border: 1.5px solid var(--ink);
    background: var(--white);
    color: var(--ink);
    font-size: 20px;
  }
  .event-date__label {
    width: 138px;
    border-right: 1.5px solid var(--ink);
    display: flex;
    align-items: center;
    padding-left: 13px;
    font-weight: 700;
  }
  .event-date__write-in { flex: 1; }
</style>
</head>
<body>
<main class="poster">
  <svg class="poster__backdrop" width="1200" height="754" viewBox="0 0 1200 754" aria-hidden="true">
    <polygon points="0,0 625,0 425,754 0,754" fill="var(--purple)"/>
  </svg>

  <div class="athlete-photo" role="img" aria-label="Photo of the visiting athlete, smiling, wearing a blue and red team tracksuit jacket"></div>

  <div class="impact-stat">
    <span class="impact-stat__number">3</span>
    <span class="impact-stat__label">million<br>children<br>inspired</span>
  </div>

  <section class="athlete-bio">
    <h2 class="athlete-bio__name">Meet Athlete Name</h2>
    <p class="athlete-bio__text">International sprinter and championship finalist, sharing the journey from school sports day to the world stage, and why being active matters.</p>
  </section>

  <h1 class="headline">Inspirational<br>athlete visiting<br>our school</h1>

  <p class="fundraiser">Sponsor our pupils and help us <strong>raise money for new PE &amp; sports equipment.</strong></p>

  <div class="pillars">
    <div class="pillar pillar--inspired">Be<br>inspired</div>
    <div class="pillar pillar--difference">Make a<br>difference</div>
    <div class="pillar pillar--active">Get<br>Active</div>
  </div>

  <div class="event-date">
    <div class="event-date__label">Event Date:</div>
    <div class="event-date__write-in" aria-label="Space for the school to write the event date"></div>
  </div>
</main>
</body>
</html>
```